Saffron Tram food box

To design a label (sticker) for my Biriyani and Curries that comply with Australian food labeling regulations for cook chilled food.

one sticker that covers all 4 sides of the box

```html
<!DOCTYPE html>
<html lang="en">
<head>
<meta charset="UTF-8">
<title>Saffron Tram – Chicken &amp; Vegitable Cottage Pie Label</title>
<link href="https://fonts.googleapis.com/css2?family=League+Gothic&family=Oswald:wght@400;500&family=Source+Serif+4:wght@300;400&family=Poppins:wght@400;500;600;700&display=swap" rel="stylesheet">
<style>
  :root{
    --page:#dcdcdc;
    --brown-deep:#3a1a12;
    --brown:#5b2418;
    --red-glow:#a8291f;
    --tab:#121010;
    --brand:#f39a2b;
    --badge-red:#e8262a;
    --green:#5aae3c;
    --ink:#1b1b1b;
    --white:#ffffff;
  }
  *{box-sizing:border-box;margin:0;padding:0}
  html,body{width:991px;height:1200px;overflow:hidden;background:var(--page)}
  .label{
    position:absolute;left:101px;top:50px;width:788px;height:1100px;overflow:hidden;
    background:
      radial-gradient(ellipse 420px 560px at 72% 52%, var(--red-glow) 0%, rgba(140,36,26,.6) 45%, rgba(0,0,0,0) 80%),
      linear-gradient(180deg, var(--brown-deep) 0%, var(--brown) 35%, var(--brown) 70%, var(--brown-deep) 100%);
    box-shadow:0 10px 24px rgba(0,0,0,.18);
    font-family:"Poppins",sans-serif;color:var(--white);
  }
  .shapes{position:absolute;inset:0}
  .brand-tab{
    position:absolute;left:0;top:51px;width:407px;height:114px;background:var(--tab);
    border-radius:0 24px 24px 0;display:flex;align-items:center;justify-content:center;gap:14px;
  }
  .brand-dot{width:30px;height:30px;border-radius:50%;background:var(--brand)}
  .brand-name{font-family:"Oswald",sans-serif;font-weight:500;font-size:44px;color:var(--brand);letter-spacing:1px}
  .title{position:absolute;left:36px;top:246px;font-family:"League Gothic","Oswald",sans-serif;font-weight:400;line-height:1;text-transform:uppercase;white-space:nowrap}
  .title span{display:block}
  .title .l1{font-size:128px;height:112px}
  .title .l2{font-size:128px;height:110px}
  .title .l3{font-size:106px}
  .description{position:absolute;left:42px;top:612px;font-family:"Source Serif 4",serif;font-weight:300;font-size:25px;line-height:26px;white-space:nowrap}
  .intake-caption{position:absolute;left:46px;top:806px;width:388px;text-align:center;font-size:13px;font-weight:600}
  .intake-pill{position:absolute;left:46px;top:824px;width:388px;height:24px;border-radius:12px;background:var(--white);color:var(--ink);font-size:13px;font-weight:600;text-align:center;line-height:24px}
  .net-weight{position:absolute;left:45px;top:882px;font-size:25px;display:flex;align-items:center;gap:8px}
  .new-badge{
    position:absolute;left:507px;top:142px;width:108px;height:108px;border-radius:50%;
    background:var(--badge-red);border:5px solid var(--white);box-shadow:0 2px 6px rgba(0,0,0,.3);
    display:flex;flex-direction:column;align-items:center;justify-content:center;font-weight:700;line-height:1;z-index:2
  }
  .new-badge .big{font-size:27px}
  .new-badge .small{font-size:19px;font-weight:600}
  .extra-strip{position:absolute;left:597px;top:142px;width:191px;height:58px;background:var(--white);color:var(--ink);display:flex;align-items:center;gap:6px;padding-left:22px}
  .extra-strip .pct{font-family:"Oswald",sans-serif;font-weight:500;font-size:32px}
  .extra-strip .words{font-size:18px;font-weight:500;line-height:1}
  .serving-note{position:absolute;left:629px;top:716px;width:110px;color:var(--ink)}
  .serving-note .tag{display:inline-block;background:rgba(255,255,255,.75);border-radius:9px;padding:2px 8px;font-size:10px;font-weight:600;white-space:nowrap}
  .serving-note .box{margin-top:3px;height:58px;border-radius:14px;background:rgba(255,255,255,.55);padding:5px 8px;font-size:10px;font-weight:600;position:relative}
  .serving-note .box i{position:absolute;left:0;bottom:0;width:22px;height:20px;background:var(--white)}
  .produced{position:absolute;left:629px;top:818px;font-size:10px;font-weight:600;color:#3b4a1c;white-space:nowrap}
  .info-row{position:absolute;left:0;top:960px;width:788px;height:90px;color:var(--ink)}
  .divider{position:absolute;top:7px;width:2px;height:77px;background:#444}
  .microwave{position:absolute;left:90px;top:8px;width:96px;text-align:center;color:var(--green)}
  .microwave .word{font-size:15px;font-weight:600}
  .microwave .time{font-size:48px;font-weight:500;line-height:1}
  .microwave .time small{font-size:18px;font-weight:400}
  .icon-circle{position:absolute;top:8px;width:74px;height:74px;border-radius:50%;border:2px solid var(--ink);background:var(--white);display:flex;flex-direction:column;align-items:center;justify-content:center;line-height:1.05}
  .serves .word{font-size:16px}
  .serves .num{font-size:28px;font-weight:700}
  .energy{font-size:15px;font-weight:500}
  .energy .per{margin-top:2px;border:1.5px solid var(--ink);border-radius:8px;padding:0 5px;font-size:11px}
  .star-badge{border:3px solid var(--ink);box-shadow:inset 0 0 0 6px var(--white), inset 0 0 0 9px #555}
  .farm-badge{background:var(--ink);box-shadow:inset 0 0 0 9px var(--ink), inset 0 0 0 100px var(--white)}
  .farm-badge::after{content:"";width:26px;height:26px;border-radius:50%;background:var(--green)}
  .origin-badge{position:absolute;left:648px;top:-17px;width:54px;height:101px;border:2px solid var(--ink);border-radius:4px;background:var(--white);box-shadow:inset 0 0 0 4px var(--white), inset 0 36px 0 4px var(--ink)}
</style>
</head>
<body>
<div class="label">
  <svg class="shapes" width="788" height="1100" viewBox="0 0 788 1100">
    <defs>
      <linearGradient id="plate-rim" x1="0" y1="0" x2="1" y2="1">
        <stop offset="0" stop-color="#ffffff"/>
        <stop offset="1" stop-color="#d9d9d9"/>
      </linearGradient>
      <linearGradient id="pie-tones" x1="0.3" y1="0" x2="0.6" y2="1">
        <stop offset="0" stop-color="#f1e6ad"/>
        <stop offset="0.38" stop-color="#e0c977"/>
        <stop offset="0.6" stop-color="#7e8a45"/>
        <stop offset="0.78" stop-color="#4f6b2c"/>
        <stop offset="0.92" stop-color="#c9743a"/>
      </linearGradient>
      <linearGradient id="swoosh" x1="0" y1="0" x2="1" y2="0">
        <stop offset="0" stop-color="#c0261f" stop-opacity="0"/>
        <stop offset="0.55" stop-color="#e2402a"/>
        <stop offset="0.8" stop-color="#f39a2b"/>
        <stop offset="1" stop-color="#5aae3c"/>
      </linearGradient>
    </defs>
    <path d="M0 936 C 220 900, 470 880, 788 772" fill="none" stroke="url(#swoosh)" stroke-width="8"/>
    <path d="M0 946 C 220 910, 470 890, 788 782 L788 1100 L0 1100 Z" fill="#ffffff"/>
    <circle cx="849" cy="477" r="425" fill="url(#plate-rim)"/>
    <circle cx="862" cy="480" r="405" fill="url(#pie-tones)" role="img" aria-label="Photo of the chicken and vegetable cottage pie in a white dish, golden mashed potato top with greens and carrot"/>
  </svg>

  <div class="brand-tab">
    <span class="brand-dot"></span>
    <span class="brand-name">Saffron Tram</span>
  </div>

  <div class="new-badge"><span class="big">NEW</span><span class="small">RECIPE</span></div>
  <div class="extra-strip"><span class="pct">30%</span><span class="words">EXTRA<br>CHICKEN</span></div>

  <h1 class="title">
    <span class="l1">Chicken &amp;</span>
    <span class="l2">Vegitable</span>
    <span class="l3">Cottage Pie</span>
  </h1>

  <p class="description">Tender, Australian chicken<br>in a thyme infused cream sauce<br>with a medley of&nbsp; onion, sweet<br>of white wine and topped with<br>pipings of creamy mashed patato.</p>

  <div class="serving-note">
    <span class="tag">Serving Suggestion</span>
    <div class="box">Keep refrigerated<i></i></div>
  </div>
  <div class="produced">Produced in the Australia</div>

  <div class="intake-caption">% of the Reference Intakes</div>
  <div class="intake-pill">Typical Values per 100g: Energy 487kj/116kcal</div>

  <div class="net-weight">350 g
    <svg width="42" height="36" viewBox="0 0 42 36"><path d="M4 18 H38 A17 16 0 1 0 33 30" fill="none" stroke="#fff" stroke-width="4"/></svg>
  </div>

  <div class="info-row">
    <div class="microwave"><div class="word">Microwave</div><div class="time">4 <small>min</small></div></div>
    <span class="divider" style="left:195px"></span>
    <div class="icon-circle serves" style="left:211px"><span class="word">serves</span><span class="num">1</span></div>
    <span class="divider" style="left:308px"></span>
    <div class="icon-circle star-badge" style="left:321px"></div>
    <span class="divider" style="left:412px"></span>
    <div class="icon-circle energy" style="left:428px"><span>Energy</span><span>497kj</span><span class="per">PER 100g</span></div>
    <span class="divider" style="left:519px"></span>
    <div class="icon-circle farm-badge" style="left:537px"></div>
    <span class="divider" style="left:631px"></span>
    <div class="origin-badge"></div>
  </div>
</div>
</body>
</html>
```